Professional Services (B-2-B) Business Cards (Front & Back)

Quintarion is a business-to-business professional services company in the legal sector. They typically present to c-suite and executive functions who are looking for providers with expertise, and experience. Our business card should look and feel professional and contemporary, but we are not a startup tech company, so we want the tone to be more mature.

```html
<!DOCTYPE html>
<html lang="en">
<head>
<meta charset="utf-8">
<title>Quintarion Business Cards</title>
<link href="https://fonts.googleapis.com/css2?family=Montserrat:wght@500;600&family=Poppins:wght@500;600&display=swap" rel="stylesheet">
<style>
  :root {
    --page-bg: #d7d7d7;
    --navy: #020d30;
    --accent: #00307a;
    --accent-soft: rgba(0, 48, 122, 0.55);
    --accent-faint: rgba(0, 48, 122, 0.16);
    --card-light: #f8f8fc;
    --ink: #020d30;
    --white: #ffffff;
  }
  html, body {
    margin: 0;
    width: 1200px;
    height: 1000px;
    overflow: hidden;
    background: var(--page-bg);
  }
  .sheet {
    position: relative;
    width: 1200px;
    height: 1000px;
  }
  .card {
    position: absolute;
    left: 385px;
    width: 429px;
    height: 238px;
    border-radius: 12px;
    overflow: hidden;
  }
  .card svg { position: absolute; left: 0; top: 0; display: block; }
  .card--front { top: 224px; background: var(--navy); }
  .card--back { top: 538px; background: var(--card-light); }

  .accent-area { position: absolute; }
  .accent-area--front-top {
    left: 245px; top: 0; width: 142px; height: 58px;
    background: linear-gradient(200deg, var(--accent-soft), rgba(0, 48, 122, 0));
  }
  .accent-area--front-bottom {
    left: 41px; top: 180px; width: 148px; height: 58px;
    background: linear-gradient(20deg, var(--accent-soft), rgba(0, 48, 122, 0));
  }
  .accent-area--back {
    right: 0; top: 0; width: 150px; height: 238px;
    background: linear-gradient(90deg, rgba(0, 48, 122, 0), var(--accent-faint) 45%, var(--accent-soft));
  }

  .brand-front {
    font-family: 'Montserrat', sans-serif;
    font-weight: 500;
    font-size: 18px;
    letter-spacing: 5px;
    fill: var(--white);
  }
  .brand-back {
    font-family: 'Montserrat', sans-serif;
    font-weight: 600;
    font-size: 8px;
    letter-spacing: 1.8px;
    fill: var(--accent);
  }
  .holder-name {
    font-family: 'Poppins', sans-serif;
    font-weight: 500;
    font-size: 46px;
    letter-spacing: 1.5px;
    fill: var(--ink);
  }
  .holder-title {
    font-family: 'Poppins', sans-serif;
    font-weight: 600;
    font-size: 19px;
    letter-spacing: 4.6px;
    fill: var(--accent);
  }
  .contact-line {
    font-family: 'Poppins', sans-serif;
    font-weight: 500;
    font-size: 9.8px;
    letter-spacing: 0.5px;
    fill: var(--ink);
  }
  .icon-box { fill: none; stroke: var(--ink); stroke-width: 1.2; }
  .icon-glyph { fill: var(--ink); }
</style>
</head>
<body>
<main class="sheet">

  <section class="card card--front" aria-label="Card front">
    <div class="accent-area accent-area--front-top" role="img" aria-label="Blue diagonal accent area"></div>
    <div class="accent-area accent-area--front-bottom" role="img" aria-label="Blue diagonal accent area"></div>
    <svg width="429" height="238" viewBox="0 0 429 238">
      <text class="brand-front" x="214" y="126" text-anchor="middle">QUINTARION</text>
    </svg>
  </section>

  <section class="card card--back" aria-label="Card back">
    <div class="accent-area accent-area--back" role="img" aria-label="Blue angled accent area"></div>
    <svg width="429" height="238" viewBox="0 0 429 238">
      <text class="brand-back" x="30" y="41">QUINTARION</text>

      <text class="holder-name" x="24" y="110">Mara Ellison</text>
      <text class="holder-title" x="26" y="137">President &amp; CEO</text>

      <g class="contact contact--mobile">
        <rect class="icon-box" x="27.5" y="171.5" width="10" height="10" rx="2.5"/>
        <rect class="icon-glyph" x="30.5" y="175" width="4" height="5" rx="0.6"/>
        <text class="contact-line" x="44" y="180">(415) 555- 0148</text>
      </g>
      <g class="contact contact--phone">
        <rect class="icon-box" x="27.5" y="187.5" width="10" height="10" rx="2.5"/>
        <path class="icon-glyph" d="M30.3 189.8c.5-.4 1.1-.3 1.3.2l.5 1.1c.2.4 0 .8-.3 1l-.4.3c.4.9 1.1 1.6 2 2l.3-.4c.2-.3.6-.5 1-.3l1.1.5c.5.2.6.8.2 1.3l-.5.5c-.5.5-1.3.6-2 .3-1.9-.8-3.4-2.3-4.2-4.2-.3-.7-.2-1.5.3-2z"/>
        <text class="contact-line" x="44" y="196">(203) 555 – 0193</text>
      </g>
      <g class="contact contact--email">
        <rect class="icon-box" x="27.5" y="203.5" width="10" height="10" rx="2.5"/>
        <path class="icon-glyph" d="M30 206.3h5l-2.5 2zM29.9 207l2.6 2.1 2.6-2.1v3.7h-5.2z"/>
        <text class="contact-line" x="44" y="212">mellison@quintarion.law</text>
      </g>
    </svg>
  </section>

</main>
</body>
</html>
```